Business Card Design Project

We need a Business Card for an Mechanical Engineering firm in Singapore. The design should be Modern & Technical looking, yet eye catching.

Our company deals in Cutting Tools & Machine Accessories for the Manufacturing Industries such as Oil & Gas, Aero Space, etc... For more information on our Company, you can either email me or view our website www.valtrion.com.sg.

We are trying to revamp our image to give our consumers a fresh new perspective to our company, so we welcome all ideas.

Industry/Entity Type

Business

Requirements
Must have
• Must incorporate New Company Logo into the card as shown in Uploaded file.

```html
<!DOCTYPE html>
<html lang="en">
<head>
<meta charset="utf-8">
<title>Valtrion Tools – Business Card</title>
<link href="https://fonts.googleapis.com/css2?family=Michroma&family=Open+Sans:wght@400&display=swap" rel="stylesheet">
<style>
  :root {
    --maroon: #9a0036;
    --maroon-dark: #4a0a24;
    --paper: #ffffff;
    --ink-light: #ffffff;
    --stage: #ecebea;
  }
  * { margin: 0; padding: 0; box-sizing: border-box; }
  html, body {
    width: 1200px;
    height: 900px;
    overflow: hidden;
    background: var(--stage);
  }
  .canvas {
    width: 1200px;
    height: 900px;
    display: flex;
    align-items: center;
    justify-content: center;
    gap: 50px;
  }
  .card {
    width: 540px;
    height: 310px;
    position: relative;
    box-shadow: 0 6px 18px rgba(0,0,0,0.18);
  }
  /* Front */
  .card--front {
    background: var(--paper);
    display: flex;
    align-items: center;
    justify-content: center;
  }
  .brand {
    display: flex;
    align-items: center;
    gap: 14px;
    font-family: "Michroma", sans-serif;
    color: var(--maroon);
  }
  .brand__dot {
    width: 34px;
    height: 34px;
    border-radius: 50%;
    background: var(--maroon);
    flex: none;
  }
  .card--front .brand__name {
    font-size: 30px;
    letter-spacing: 1px;
  }
  /* Back */
  .card--back {
    background: var(--maroon);
    color: var(--ink-light);
  }
  .card--back .brand {
    position: absolute;
    left: 34px;
    top: 40px;
    color: var(--ink-light);
    gap: 8px;
  }
  .card--back .brand__dot {
    width: 14px;
    height: 14px;
    background: var(--ink-light);
  }
  .card--back .brand__name {
    font-size: 13px;
    letter-spacing: 0.5px;
  }
  .divider {
    position: absolute;
    left: 220px;
    top: 110px;
    width: 2px;
    height: 150px;
    background: var(--ink-light);
  }
  .contact {
    position: absolute;
    left: 246px;
    top: 112px;
  }
  .contact__name {
    font-family: "Michroma", sans-serif;
    font-size: 18px;
    letter-spacing: 0.5px;
    margin-bottom: 12px;
  }
  .contact__list {
    list-style: none;
    font-family: "Open Sans", sans-serif;
    font-size: 13px;
    line-height: 24px;
  }
  .contact__label {
    display: inline-block;
    width: 26px;
  }
</style>
</head>
<body>
  <main class="canvas">
    <section class="card card--front" aria-label="Card front">
      <div class="brand">
        <span class="brand__dot" aria-hidden="true"></span>
        <span class="brand__name">VALTRION TOOLS</span>
      </div>
    </section>

    <section class="card card--back" aria-label="Card back">
      <div class="brand">
        <span class="brand__dot" aria-hidden="true"></span>
        <span class="brand__name">VALTRION TOOLS</span>
      </div>
      <div class="divider" aria-hidden="true"></div>
      <div class="contact">
        <h1 class="contact__name">MARCUS HALE</h1>
        <ul class="contact__list">
          <li><span class="contact__label">t :</span>6345 2710</li>
          <li><span class="contact__label">f :</span>6345 2711</li>
          <li><span class="contact__label">e :</span>daniel.wong@valtrion.com</li>
          <li><span class="contact__label">w :</span>http://www.valtriontools.com</li>
        </ul>
      </div>
    </section>
  </main>
</body>
</html>
```